Doctors Office Web Design

Name of the business is Lin-Yue Hart M.D.
We need a web design that is attractive for women that want to see Dr. Lin-Yue Hart for Obstetrician Gynecology and Pregnancy care. Dr. Hart earned her degree from Carrow Ridge Medical College of obstetrician gynecology. We want to attract women of child bearing ages to come to our offices for health, education, and pregnancies.

Please visit http://www.drhartclinicweb.com/ to help you get a feel for who we are. We will be adding some pictures and logo in the next few days.

We are looking for to have pages for and tabs including
About Us- History, Our Staff, Dr. Hart
Patient Information- Appointments, E-Prescriptions, Payments Accepted, Insurance
Health- General, Sexual, Mental, Affiliates
Pregnancy- Minimally invasive surgery(our specialty), 4-D Ultra Sound, Hospital Affiliations
Media- News,Pictures, Videos
Locations- Palmer Office, Westvale Office

The colors we would like to use are pastel colors, magenta, and plum

Target Market(s)

Women of all ages with an emphasis on 25-65 year olds

Industry/Entity Type

Business

Requirements
Must have
• Needs to include a location for a our videos and pictures that I will submit shortly. We also want a map to our location or atleast a place for one.
Nice to have
• A place for a google map of our office locations.

```html
<!DOCTYPE html>
<html lang="en">
<head>
<meta charset="utf-8">
<title>Dr. Lin-Yue Hart M.D. – Obstetrician/Gynecologist</title>
<link href="https://fonts.googleapis.com/css2?family=Merriweather:wght@700;900&family=Lustria&family=Open+Sans:wght@400;600;700&display=swap" rel="stylesheet">
<style>
  :root {
    --plum-dark: #5a001c;
    --plum: #6e0a2c;
    --tab: #8a1d47;
    --tab-hover: #9a2655;
    --magenta-band: #861641;
    --heading: #7c123a;
    --body-text: #2a2a2a;
    --content-bg: #f6f3f4;
    --footer-bg: #393435;
    --white: #ffffff;
    --divider: #b2557a;
  }
  * { margin: 0; padding: 0; box-sizing: border-box; }
  html, body { width: 1200px; height: 1140px; overflow: hidden; background: var(--white); }
  .page { position: relative; width: 1200px; height: 1140px; font-family: "Open Sans", Arial, sans-serif; }

  /* Header */
  .site-header {
    position: absolute; left: 0; top: 0; width: 1200px; height: 180px;
    background: radial-gradient(ellipse 260px 90px at 980px 170px, #8c2a4d 0%, rgba(140,42,77,0) 100%),
                linear-gradient(180deg, var(--plum) 0%, var(--plum-dark) 100%);
  }
  .header-rule { position: absolute; left: 0; top: 180px; width: 1200px; height: 6px; background: #dcdcdc; border-top: 2px solid var(--white); }
  .main-nav { position: absolute; left: 86px; top: 0; display: flex; gap: 2px; }
  .main-nav a {
    display: block; width: 145px; height: 56px; line-height: 62px; text-align: center;
    background: var(--tab); color: #f4dce5; text-decoration: none;
    font-weight: 700; font-size: 17px; letter-spacing: 0.3px; border-radius: 0 0 5px 5px;
  }
  .main-nav a.is-active { color: var(--white); border-top: 9px solid var(--white); line-height: 44px; }
  .brand { position: absolute; left: 100px; top: 100px; color: var(--white); }
  .brand-name { font-family: "Merriweather", Georgia, serif; font-weight: 900; font-size: 33px; letter-spacing: 0.5px; }
  .brand-name small { font-family: "Open Sans", Arial, sans-serif; font-size: 15px; font-weight: 700; margin-left: 8px; }
  .brand-tagline { font-size: 13.5px; font-weight: 700; margin-top: 6px; margin-left: 3px; }

  /* Content */
  .content { position: absolute; left: 0; top: 186px; width: 1200px; height: 545px; background: var(--content-bg); }
  .welcome-title { position: absolute; left: 96px; top: 32px; font-size: 29px; font-weight: 400; color: var(--heading); }
  .welcome-text { position: absolute; left: 101px; top: 84px; width: 700px; font-size: 18px; line-height: 34px; color: var(--body-text); }
  .welcome-text .email { color: #111; font-weight: 600; }

  .services-box {
    position: absolute; left: 102px; top: 253px; width: 661px; height: 267px;
    background: #f3f1f1; box-shadow: 3px 3px 4px rgba(0,0,0,0.35);
  }
  .services-photo { position: absolute; left: 0; top: 41px; width: 148px; height: 226px;
    background: linear-gradient(160deg, #efe5e0 0%, #e7d9d4 50%, #f4efed 100%); }
  .services-title { position: absolute; left: 130px; top: 14px; font-family: "Lustria", Georgia, serif; font-size: 23px; color: var(--heading); }
  .services-list { position: absolute; left: 255px; top: 62px; list-style: none; }
  .services-list li { font-family: "Lustria", Georgia, serif; font-size: 20px; color: var(--heading); height: 36px; display: flex; align-items: center; }
  .services-list li::before { content: ""; border-left: 9px solid #222; border-top: 5px solid transparent; border-bottom: 5px solid transparent; margin-right: 12px; }

  .doctor-glow { position: absolute; left: 760px; top: 30px; width: 420px; height: 500px;
    background: radial-gradient(ellipse 200px 240px at 200px 240px, #f7cfe0 0%, rgba(247,207,224,0) 100%); }
  .doctor-photo { position: absolute; left: 820px; top: 38px; width: 308px; height: 462px;
    background: linear-gradient(180deg, #e6e8ee 0%, #dfe5ef 40%, #c9d3e2 100%); }

  /* Contact band */
  .info-band { position: absolute; left: 0; top: 726px; width: 1200px; height: 340px; background: var(--magenta-band); }
  .zigzag { position: absolute; left: 0; top: 720px; }
  .section-icon { position: absolute; width: 56px; height: 58px; }
  .section-title { position: absolute; font-family: "Merriweather", Georgia, serif; font-weight: 700; font-size: 22px; color: var(--white); letter-spacing: 0.5px; }
  .location-map { position: absolute; left: 107px; top: 85px; width: 170px; height: 160px;
    border: 4px solid #cfc7cc; background: linear-gradient(135deg, #eef3fb 0%, #c9d7ee 100%); }
  .address { position: absolute; left: 311px; top: 86px; font-style: normal; color: var(--white); font-size: 19px; line-height: 29px; text-transform: uppercase; }
  .band-divider { position: absolute; left: 700px; top: 37px; width: 1px; height: 271px; background: var(--divider); }
  .video-player { position: absolute; left: 802px; top: 84px; width: 282px; height: 234px; background: #000; }
  .video-brand { position: absolute; right: 8px; bottom: 26px; color: #9a9a9a; font-size: 12px; font-weight: 700; }
  .video-controls { position: absolute; left: 0; bottom: 0; width: 282px; height: 16px; background: linear-gradient(#eee, #c9c9c9); }

  /* Footer */
  .site-footer { position: absolute; left: 0; top: 1066px; width: 1200px; height: 74px; background: var(--footer-bg); }
  .footer-nav { position: absolute; left: 89px; top: 28px; font-size: 17px; color: #cfcfcf; }
  .footer-nav a { color: #cfcfcf; text-decoration: none; }
  .footer-nav a.is-active { color: var(--white); }
  .footer-nav .sep { margin: 0 9px; color: #9a9a9a; }
  .copyright { position: absolute; left: 1032px; top: 17px; font-size: 13px; color: var(--white); }
</style>
</head>
<body>
<div class="page">
  <header class="site-header">
    <nav class="main-nav">
      <a class="is-active" href="#">HOME</a>
      <a href="#">ABOUT US</a>
      <a href="#">PATIENT INFO</a>
      <a href="#">HEALTH</a>
      <a href="#">PREGNANCY</a>
      <a href="#">MEDIA</a>
      <a href="#">LOCATIONS</a>
    </nav>
    <div class="brand">
      <div class="brand-name">Dr. Lin-Yue Hart<small>M.D.</small></div>
      <div class="brand-tagline">Facog board certified&nbsp; Obstetrician/Gynecologist</div>
    </div>
  </header>
  <div class="header-rule"></div>

  <main class="content">
    <h1 class="welcome-title">Welcome to Dr. Lin-Yue Hart's website.</h1>
    <p class="welcome-text">Here you will be able to find information about both of our offices, meet Dr. Hart and her staff, and browse through our women's health links to learn more about pregnancy, nutrition, exercise, and other women's health issues. Serving Have fun and if you have any questions, feel free to contact us at <span class="email">drhart@westvalemail.net</span></p>

    <section class="services-box">
      <div class="services-photo" role="img" aria-label="Photo of a pregnant woman seated, holding her belly"></div>
      <h2 class="services-title">Serving all areas of women's health, including:</h2>
      <ul class="services-list">
        <li>OBSTETRICS</li>
        <li>FAMILY PLANNING</li>
        <li>HORMONAL EVALUATION</li>
        <li>INCONTINENCE, INFERTILITY</li>
        <li>GYNECOLOGY SURGERY</li>
      </ul>
    </section>

    <div class="doctor-glow"></div>
    <div class="doctor-photo" role="img" aria-label="Photo of a smiling doctor in a white coat holding a folder"></div>
  </main>

  <section class="info-band">
    <svg class="section-icon" style="left:100px;top:14px" viewBox="0 0 56 58" aria-hidden="true">
      <circle cx="28" cy="29" r="27" fill="#5a0a26"/>
      <circle cx="28" cy="29" r="23" fill="#7a1238"/>
      <rect x="14" y="19" width="28" height="20" fill="#f4b9cf"/>
      <polyline points="14,19 28,31 42,19" fill="none" stroke="#7a1238" stroke-width="1.6"/>
    </svg>
    <h2 class="section-title" style="left:179px;top:32px">CONTACT &amp; LOCATION</h2>

    <div class="location-map" role="img" aria-label="Road map to the office location"></div>
    <address class="address">
      2480 Orchard Crest Avenue<br>
      Suite 210-211<br>
      Westvale Bay, Florida&nbsp; 33910<br>
      Tel:&nbsp; (555) 218-4470<br>
      Fax: (555) 218-4471
    </address>

    <div class="band-divider"></div>

    <svg class="section-icon" style="left:790px;top:14px" viewBox="0 0 56 58" aria-hidden="true">
      <circle cx="28" cy="29" r="27" fill="#5a0a26"/>
      <circle cx="28" cy="29" r="23" fill="#7a1238"/>
      <rect x="15" y="24" width="19" height="14" rx="2" fill="#f4b9cf"/>
      <polygon points="34,28 42,23 42,39 34,34" fill="#f4b9cf"/>
      <circle cx="20" cy="20" r="4" fill="#f4b9cf"/>
      <circle cx="29" cy="20" r="4" fill="#f4b9cf"/>
    </svg>
    <h2 class="section-title" style="left:866px;top:32px">OUR VIDEOS</h2>

    <div class="video-player">
      <svg style="position:absolute;left:117px;top:96px" width="48" height="34" viewBox="0 0 48 34" aria-hidden="true">
        <rect x="1" y="1" width="46" height="32" rx="6" fill="#8a8a8a" stroke="#5a5a5a"/>
        <polygon points="18,9 32,17 18,25" fill="#2a2a2a"/>
      </svg>
      <span class="video-brand">ClipStream</span>
      <div class="video-controls">
        <svg width="282" height="16" viewBox="0 0 282 16" aria-hidden="true">
          <polygon points="6,4 12,8 6,12" fill="#222"/>
          <rect x="18" y="6" width="170" height="4" rx="2" fill="#9a9a9a"/>
          <circle cx="22" cy="8" r="4" fill="#555"/>
          <text x="205" y="11" font-size="7" fill="#444" font-family="Arial, sans-serif">0:00 / 0:00</text>
          <rect x="244" y="5" width="8" height="6" fill="#333"/>
          <rect x="262" y="4" width="14" height="8" fill="#333"/>
        </svg>
      </div>
    </div>
  </section>

  <svg class="zigzag" width="1200" height="12" viewBox="0 0 1200 12" aria-hidden="true">
    <polygon fill="#861641" points="0,6 6,0 12,6 18,0 24,6 30,0 36,6 42,0 48,6 54,0 60,6 66,0 72,6 78,0 84,6 90,0 96,6 102,0 108,6 114,0 120,6 126,0 132,6 138,0 144,6 150,0 156,6 162,0 168,6 174,0 180,6 186,0 192,6 198,0 204,6 210,0 216,6 222,0 228,6 234,0 240,6 246,0 252,6 258,0 264,6 270,0 276,6 282,0 288,6 294,0 300,6 306,0 312,6 318,0 324,6 330,0 336,6 342,0 348,6 354,0 360,6 366,0 372,6 378,0 384,6 390,0 396,6 402,0 408,6 414,0 420,6 426,0 432,6 438,0 444,6 450,0 456,6 462,0 468,6 474,0 480,6 486,0 492,6 498,0 504,6 510,0 516,6 522,0 528,6 534,0 540,6 546,0 552,6 558,0 564,6 570,0 576,6 582,0 588,6 594,0 600,6 606,0 612,6 618,0 624,6 630,0 636,6 642,0 648,6 654,0 660,6 666,0 672,6 678,0 684,6 690,0 696,6 702,0 708,6 714,0 720,6 726,0 732,6 738,0 744,6 750,0 756,6 762,0 768,6 774,0 780,6 786,0 792,6 798,0 804,6 810,0 816,6 822,0 828,6 834,0 840,6 846,0 852,6 858,0 864,6 870,0 876,6 882,0 888,6 894,0 900,6 906,0 912,6 918,0 924,6 930,0 936,6 942,0 948,6 954,0 960,6 966,0 972,6 978,0 984,6 990,0 996,6 1002,0 1008,6 1014,0 1020,6 1026,0 1032,6 1038,0 1044,6 1050,0 1056,6 1062,0 1068,6 1074,0 1080,6 1086,0 1092,6 1098,0 1104,6 1110,0 1116,6 1122,0 1128,6 1134,0 1140,6 1146,0 1152,6 1158,0 1164,6 1170,0 1176,6 1182,0 1188,6 1194,0 1200,6 1200,12 0,12"/>
  </svg>

  <footer class="site-footer">
    <nav class="footer-nav">
      <a class="is-active" href="#">Home</a><span class="sep">|</span><a href="#">About Us</a><span class="sep">|</span><a href="#">Patient Info</a><span class="sep">|</span><a href="#">Health</a><span class="sep">|</span><a href="#">Pregnancy</a><span class="sep">|</span><a href="#">Media</a><span class="sep">|</span><a href="#">Locations</a>
    </nav>
    <div class="copyright">Copyright 2011</div>
  </footer>
</div>
</body>
</html>
```